A4 Menu needed for cafe - attached design

Need an A4 menu designed for our cafe.
I have attached our catering menu - I would like the new menu to be designed in the exact same way.

I have attached the text that needs to appear on the menu

Industry/Entity Type

Catering

```html
<!DOCTYPE html>
<html lang="en">
<head>
<meta charset="utf-8">
<title>Morning Rounds – Catering Menu</title>
<link rel="stylesheet" href="https://fonts.googleapis.com/css2?family=Courier+Prime:wght@400;700&family=Oswald:wght@500;600&family=Arimo&display=swap">
<style>
  :root {
    --board: #1c1c1c;
    --board-light: #262626;
    --chalk: #f2f2ee;
    --chalk-soft: #dcdcd6;
    --lemon: #fbf3a0;
    --lemon-text: #e9df7e;
    --ribbon-line: #d9d29a;
    --ink: #3a2f2c;
  }
  * { margin: 0; padding: 0; box-sizing: border-box; }
  html, body { width: 1200px; height: 848px; overflow: hidden; }
  body {
    background: radial-gradient(ellipse at 50% 40%, var(--board-light), var(--board) 75%);
    color: var(--chalk);
    font-family: "Courier Prime", "Courier New", monospace;
    position: relative;
  }
  .brand-tile {
    position: absolute; left: 512px; top: 43px; width: 174px; height: 151px;
    background: var(--lemon);
    display: flex; align-items: center; justify-content: center;
  }
  .brand-name {
    font-family: "Courier Prime", "Courier New", monospace;
    font-size: 21px; font-weight: 400; color: var(--ink);
    text-align: center; line-height: 1.25; letter-spacing: 1px;
  }
  .menu-title {
    position: absolute; top: 214px; left: 0; width: 1200px;
    text-align: center; font-size: 22px; color: var(--lemon-text);
  }
  .menu-box {
    position: absolute; border: 2px solid var(--chalk);
  }
  .section-ribbon {
    position: absolute; left: 50%; top: -22px; transform: translateX(-50%);
    width: 274px; height: 40px;
  }
  .section-ribbon svg { position: absolute; inset: 0; }
  .section-ribbon h2 {
    position: relative; line-height: 40px; text-align: center;
    font-family: "Oswald", "Arial Narrow", sans-serif; font-weight: 600;
    font-size: 17px; letter-spacing: 1.5px; color: var(--chalk);
  }
  .item-list { list-style: none; position: absolute; }
  .item-list li { display: flex; }
  .item-list .name { flex: 0 0 auto; }
  .item-list .price { position: absolute; }
  .breakfast { left: 88px; top: 295px; width: 496px; height: 247px; }
  .lunch { left: 88px; top: 584px; width: 496px; height: 239px; }
  .light { left: 629px; top: 294px; width: 478px; height: 478px; }
  .compact { left: 48px; font-size: 14px; line-height: 15.7px; }
  .compact li { position: relative; width: 420px; }
  .compact .price { left: 303px; }
  .breakfast .compact { top: 42px; }
  .lunch .compact { top: 38px; }
  .spaced { left: 97px; top: 50px; font-size: 14.5px; line-height: 31.4px; }
  .spaced li { position: relative; width: 340px; }
  .spaced .price { left: 243px; }
  .contact-note {
    position: absolute; left: 628px; top: 801px; width: 482px;
    font-family: "Arimo", Arial, sans-serif; font-size: 9.6px; color: var(--chalk-soft);
    white-space: nowrap;
  }
</style>
</head>
<body>
  <div class="brand-tile">
    <span class="brand-name">MORNING<br>ROUNDS</span>
  </div>
  <h1 class="menu-title">catering menu</h1>

  <section class="menu-box breakfast">
    <div class="section-ribbon">
      <svg width="274" height="40" viewBox="0 0 274 40" aria-hidden="true">
        <path d="M1 3 H273 L259 20 L273 37 H1 L15 20 Z" fill="var(--board)" stroke="var(--ribbon-line)" stroke-width="1.6"/>
        <path d="M15 8 V32 M259 8 V32" stroke="var(--ribbon-line)" stroke-width="1.2"/>
      </svg>
      <h2>BREAKFAST</h2>
    </div>
    <ul class="item-list compact">
      <li><span class="name">Toast</span><span class="price">$2 per slice</span></li>
      <li><span class="name">Raisin Toast</span><span class="price">$2 per slice</span></li>
      <li><span class="name">Egg Bacon and Cheese Roll</span><span class="price">$6.5</span></li>
      <li><span class="name">Veggie Brekky Wrap</span><span class="price">$6.5</span></li>
      <li><span class="name">Ham and Cheese French Toast</span><span class="price">$6.5</span></li>
      <li><span class="name">Ham and Cheese Toastie</span><span class="price">$5.5</span></li>
      <li><span class="name">Cheese and Tomato Toastie</span><span class="price">$5.5</span></li>
      <li><span class="name">Ham and Cheese Croissant</span><span class="price">$6.5</span></li>
      <li><span class="name">Cheese and Tomato Croissant</span><span class="price">$6.0</span></li>
      <li><span class="name">Ham Cheese and Tomato Toastie</span><span class="price">$6.0</span></li>
      <li><span class="name">Plain Croissant</span><span class="price">$3.5</span></li>
    </ul>
  </section>

  <section class="menu-box lunch">
    <div class="section-ribbon">
      <svg width="274" height="40" viewBox="0 0 274 40" aria-hidden="true">
        <path d="M1 3 H273 L259 20 L273 37 H1 L15 20 Z" fill="var(--board)" stroke="var(--ribbon-line)" stroke-width="1.6"/>
        <path d="M15 8 V32 M259 8 V32" stroke="var(--ribbon-line)" stroke-width="1.2"/>
      </svg>
      <h2>LUNCH</h2>
    </div>
    <ul class="item-list compact">
      <li><span class="name">Pre made Sandwiches</span><span class="price">$6.5/$7.5</span></li>
      <li><span class="name">Pre made Focaccias</span><span class="price">$8.5</span></li>
      <li><span class="name">Pre made Wraps</span><span class="price">$7.5</span></li>
      <li><span class="name">Pre made Mini Rolls</span><span class="price">$4.0</span></li>
      <li><span class="name">Pre made Baguettes</span><span class="price">$9.0</span></li>
      <li><span class="name">Pre made Bagels</span><span class="price">$9.0</span></li>
      <li><span class="name">Fresh Salads made daily</span><span class="price">$9.5</span></li>
      <li><span class="name">Hot Chips</span><span class="price">$4.5</span></li>
      <li><span class="name">Plain Hamburger</span><span class="price">$7.5</span></li>
      <li><span class="name">Hamburger with the Lot</span><span class="price">$9.0</span></li>
      <li><span class="name">Chicken Schnitzel Burger</span><span class="price">$8.5</span></li>
    </ul>
  </section>

  <section class="menu-box light">
    <div class="section-ribbon">
      <svg width="274" height="40" viewBox="0 0 274 40" aria-hidden="true">
        <path d="M1 3 H273 L259 20 L273 37 H1 L15 20 Z" fill="var(--board)" stroke="var(--ribbon-line)" stroke-width="1.6"/>
        <path d="M15 8 V32 M259 8 V32" stroke="var(--ribbon-line)" stroke-width="1.2"/>
      </svg>
      <h2>SOMETHING LIGHT</h2>
    </div>
    <ul class="item-list spaced">
      <li><span class="name">Mixed Yoghurts</span><span class="price">$5.5</span></li>
      <li><span class="name">Granola and Fruit Yoghurt</span><span class="price">$5.5</span></li>
      <li><span class="name">Chia Pudding</span><span class="price">$5.5</span></li>
      <li><span class="name">Bircher Muesli</span><span class="price">$5.5</span></li>
      <li><span class="name">Fruit Salad</span><span class="price">$5.5</span></li>
      <li><span class="name">Banana Bread</span><span class="price">$4.5</span></li>
      <li><span class="name">Muffins - made fresh daily</span><span class="price">$4.5</span></li>
      <li><span class="name">Slices</span><span class="price">$4.0</span></li>
      <li><span class="name">Cookies</span><span class="price">$4.0</span></li>
      <li><span class="name">Choc Crunch Energy Bite</span><span class="price">$4.0</span></li>
      <li><span class="name">Super Crunch Energy Bite</span><span class="price">$4.0</span></li>
      <li><span class="name">Chocolate Bar</span><span class="price">$3.0</span></li>
      <li><span class="name">Packet of Chips</span><span class="price">$3.0</span></li>
    </ul>
  </section>

  <p class="contact-note">Visit us instore to discuss catering options, or call 0412 555 019 or email jo@morningroundscafe.com</p>
</body>
</html>
```